Corporate brochure design 4 pages

Hi,

We are a real estate company based in Europe.

We have almost finalized a rebranding.

We are developing a brand book guidelines (still on working process) to help you undertstand the look and feel of our new CI. I would like to receive proposals of design for a corporate brochure template. I need to receive the Indesign files with full ownership rights to be able to adapt all our documentation with this template.
Regarding the images, you can take gabaris on www.pelvaromedia.com. I will be able to take them afterwards.

There will be 4 pages. you will receive the 4 pages on pdf for your consideration with our (almost) actual layout.

- 1st page: cover
- 2nd page: company presentation in french and english
- 3rd page: some market data + graph
- 4th page: 2 retail centers presentation.

In the template, i need to have:
- the paragraph styles in order
- 2 different masters with top/bottom/page number aso.

Please feel free to ask any other questions.

best regards,
Updates

I would like to precise tha t we are active on the commercial real estate sector:

- office transactions (rent /sales)
- property management of administrative and business buildings
- Valuation of properties
- Capital markets (investment advices for selling building)

Industry/Entity Type

Real Estate

Colors

Designer to choose colors to be used in the design.

```html
<!DOCTYPE html>
<html lang="fr">
<head>
<meta charset="utf-8">
<title>Luxembourg Office Market Report Q3-2013 – Stock</title>
<link href="https://fonts.googleapis.com/css2?family=Montserrat:wght@800&family=Mulish:wght@400;600;700&display=swap" rel="stylesheet">
<style>
  :root {
    --orange: #f26a21;
    --red: #e8452c;
    --peach: #fdeee4;
    --ink: #1e1e1e;
    --grey: #6d6e71;
    --white: #ffffff;
  }
  * { margin: 0; padding: 0; box-sizing: border-box; }
  html, body { width: 848px; height: 1200px; overflow: hidden; background: var(--white); }
  body { position: relative; font-family: "Mulish", Arial, sans-serif; color: var(--ink); }

  .page-header {
    position: absolute; left: 0; top: 37px; width: 848px; height: 37px;
    background: var(--orange); color: var(--white);
    display: flex; align-items: center; gap: 24px; padding-left: 44px;
    font-size: 15.5px;
  }

  .intro-col { position: absolute; top: 84px; width: 364px; }
  .intro-col.fr { left: 43px; }
  .intro-col.en { left: 442px; }
  .section-title {
    font-family: "Montserrat", Arial, sans-serif; font-weight: 800;
    font-size: 32px; letter-spacing: 0.5px; line-height: 1;
    display: inline-block; padding-bottom: 2px;
  }
  .intro-col.fr .section-title { border-bottom: 3px solid var(--orange); }
  .intro-text {
    margin-top: 30px; font-size: 15px; line-height: 26px; color: var(--grey);
  }
  .intro-col.fr .intro-text { text-align: justify; }

  .stock-table {
    position: absolute; left: 43px; top: 299px; width: 763px;
    border-collapse: collapse; font-size: 12.5px;
  }
  .stock-table td { height: 22.8px; padding: 0 8px; white-space: nowrap; }
  .stock-table tr:nth-child(odd) td { background: var(--peach); }
  .stock-table .area { width: 287px; }
  .stock-table .district { width: 230px; }
  .stock-table .num { text-align: right; }
  .stock-table .sub td { color: var(--orange); font-weight: 700; }
  .stock-table .sub .label { text-align: right; }
  .stock-table .sub .num { font-size: 15.5px; }

  .grand-total {
    position: absolute; left: 43px; top: 832px; width: 763px; height: 24px;
    background: var(--peach); color: var(--orange); font-weight: 700;
    font-size: 14px; display: flex; align-items: center;
  }
  .grand-total .label { margin-left: 244px; }
  .grand-total .value { margin-left: 240px; font-size: 15px; }

  .stock-chart { position: absolute; left: 0; top: 880px; }

  .page-footer {
    position: absolute; left: 0; top: 1150px; width: 848px; height: 3px; background: var(--orange);
  }
  .page-number {
    position: absolute; left: 405px; top: 1132px; width: 40px; height: 40px; border-radius: 50%;
    background: var(--orange); color: var(--ink);
    font-family: "Montserrat", Arial, sans-serif; font-weight: 800; font-size: 24px;
    display: flex; align-items: center; justify-content: center;
  }
</style>
</head>
<body>
  <header class="page-header">
    <span>Rapport De Marché Bureaux Luxembourg Q3-2013</span>
    <span>Luxembourg Office Market Report Q3-2013</span>
  </header>

  <section class="intro-col fr">
    <h1 class="section-title">STOCK</h1>
    <p class="intro-text">Le stock de mètres carrés disponibles de bureaux a augmenté de 0,36 % au troisième trimestre de cette année grâce à la livraison de près de 12 300 m . Le stock total équivaut à 3 465 600 m .</p>
  </section>
  <section class="intro-col en">
    <h1 class="section-title">STOCK</h1>
    <p class="intro-text">The stock of available office square meters has increased by 0.36% during the third quarter of this year with the delivery of 12,300 m . The total stock reaches 3,465,600 sm .</p>
  </section>

  <table class="stock-table">
    <tr><td class="area"></td><td class="district">QUARTIERS-DISTRICTS</td><td class="num">STOCK M²</td><td class="num">STOCK %</td></tr>
    <tr><td>CENTRE-VILLE (CITY)</td><td>Kirchberg</td><td class="num">915 000</td><td class="num">26,42 %</td></tr>
    <tr><td></td><td>CBD</td><td class="num">806 400</td><td class="num">23,27 %</td></tr>
    <tr><td></td><td>Station</td><td class="num">382 700</td><td class="num">11,04 %</td></tr>
    <tr><td></td><td>Cloche d'Or</td><td class="num">365 600</td><td class="num">10,55 %</td></tr>
    <tr><td></td><td>Limpertsberg</td><td class="num">85 000</td><td class="num">2,45 %</td></tr>
    <tr><td></td><td>Belair / Merl</td><td class="num">67 800</td><td class="num">1,96 %</td></tr>
    <tr><td></td><td>Hamm</td><td class="num">44 500</td><td class="num">1,28 %</td></tr>
    <tr><td></td><td>Kalchesbrück</td><td class="num">33 000</td><td class="num">0,95 %</td></tr>
    <tr class="sub"><td class="label">TOTAL</td><td></td><td class="num">2 700 500</td><td class="num">77,92 %</td></tr>
    <tr><td>VILLE-PÉRIPHÉRIE (CITY-PERIPHERY)</td><td>Airport - Findel</td><td class="num">157 500</td><td class="num">4,54 %</td></tr>
    <tr><td></td><td>Bertrange / Bourmicht</td><td class="num">82 000</td><td class="num">2,37 %</td></tr>
    <tr><td></td><td>Strassen</td><td class="num">81 050</td><td class="num">2,34 %</td></tr>
    <tr><td></td><td>Howald</td><td class="num">62 600</td><td class="num">1,81 %</td></tr>
    <tr class="sub"><td class="label">TOTAL</td><td></td><td class="num">383 150</td><td class="num">11,06 %</td></tr>
    <tr><td>PÉRIPHÉRIE (PERIPHERY)</td><td>Belval</td><td class="num">93 090</td><td class="num">2,69 %</td></tr>
    <tr><td></td><td>Capellen</td><td class="num">69 500</td><td class="num">2,01 %</td></tr>
    <tr><td></td><td>Leudelange</td><td class="num">73 556</td><td class="num">2,12 %</td></tr>
    <tr><td></td><td>Munsbach</td><td class="num">60 100</td><td class="num">1,73 %</td></tr>
    <tr><td></td><td>Windhof</td><td class="num">40 600</td><td class="num">1,17 %</td></tr>
    <tr><td></td><td>Esch-sur-Alzette</td><td class="num">24 700</td><td class="num">0,71 %</td></tr>
    <tr><td></td><td>Contern</td><td class="num">20 400</td><td class="num">0,59 %</td></tr>
    <tr class="sub"><td class="label">TOTAL</td><td></td><td class="num">381 946</td><td class="num">11,02 %</td></tr>
  </table>

  <div class="grand-total"><span class="label">TOTAL</span><span class="value">3 465 596</span></div>

  <svg class="stock-chart" width="848" height="270" viewBox="0 880 848 270" font-family="Mulish, Arial, sans-serif">
    <g stroke="#bbbbbb" stroke-width="0.8" stroke-dasharray="2 2">
      <line x1="220" y1="923" x2="648" y2="923"/><line x1="220" y1="950.3" x2="648" y2="950.3"/>
      <line x1="220" y1="977.7" x2="648" y2="977.7"/><line x1="220" y1="1005" x2="648" y2="1005"/>
      <line x1="220" y1="1032.3" x2="648" y2="1032.3"/><line x1="220" y1="1059.7" x2="648" y2="1059.7"/>
      <line x1="258" y1="923" x2="258" y2="1087"/><line x1="297" y1="923" x2="297" y2="1087"/>
      <line x1="335" y1="923" x2="335" y2="1087"/><line x1="374" y1="923" x2="374" y2="1087"/>
      <line x1="412" y1="923" x2="412" y2="1087"/><line x1="451" y1="923" x2="451" y2="1087"/>
      <line x1="489" y1="923" x2="489" y2="1087"/><line x1="528" y1="923" x2="528" y2="1087"/>
      <line x1="566" y1="923" x2="566" y2="1087"/><line x1="605" y1="923" x2="605" y2="1087"/>
    </g>
    <line x1="220" y1="1087" x2="648" y2="1087" stroke="#444" stroke-width="1"/>
    <g font-size="7.5" fill="#444" text-anchor="end">
      <text x="212" y="926">3,500</text><text x="212" y="953">3,200</text>
      <text x="212" y="980">2,900</text><text x="212" y="1008">2,600</text>
      <text x="212" y="1035">2,300</text><text x="212" y="1062">2,000</text>
      <text x="212" y="1090">1,700</text>
    </g>
    <circle cx="225" cy="898" r="10" fill="var(--red)"/>
    <text x="225" y="897" font-size="6" fill="#fff" text-anchor="middle">'000</text>
    <text x="225" y="904" font-size="6" fill="#fff" text-anchor="middle">m²</text>
    <g fill="var(--orange)">
      <rect x="223" y="1040.4" width="32" height="46.6"/><rect x="261" y="1022.4" width="32" height="64.6"/>
      <rect x="300" y="1006.8" width="32" height="80.2"/><rect x="338" y="1005" width="32" height="82"/>
      <rect x="377" y="989.5" width="32" height="97.5"/><rect x="415" y="976.6" width="32" height="110.4"/>
      <rect x="454" y="953.1" width="32" height="133.9"/><rect x="492" y="948.1" width="32" height="138.9"/>
      <rect x="531" y="939.3" width="32" height="147.7"/><rect x="569" y="931.6" width="32" height="155.4"/>
      <rect x="608" y="926.2" width="32" height="160.8"/>
    </g>
    <g font-size="7.5" fill="var(--red)" text-anchor="middle">
      <text x="239" y="1037">2,211</text><text x="277" y="1019">2,409</text>
      <text x="316" y="1003">2,580</text><text x="354" y="1001">2,600</text>
      <text x="393" y="986">2,770</text><text x="431" y="973">2,912</text>
      <text x="470" y="950">3,170</text><text x="508" y="945">3,225</text>
      <text x="547" y="936">3,321</text><text x="585" y="928">3,406</text>
      <text x="624" y="922">3,465</text>
    </g>
    <g font-size="7.5" fill="#444" text-anchor="middle">
      <text x="239" y="1100">2003</text><text x="277" y="1100">2004</text>
      <text x="316" y="1100">2005</text><text x="354" y="1100">2006</text>
      <text x="393" y="1100">2007</text><text x="431" y="1100">2008</text>
      <text x="470" y="1100">2009</text><text x="508" y="1100">2010</text>
      <text x="547" y="1100">2011</text><text x="585" y="1100">2012</text>
      <text x="624" y="1100">YTD 2013</text>
    </g>
    <line x1="577" y1="1118" x2="577" y2="1140" stroke="#999" stroke-width="0.8" stroke-dasharray="1.5 1.5"/>
    <rect x="580" y="1124" width="64" height="10" fill="var(--orange)"/>
    <text x="580" y="1146" font-size="6.5" fill="#444">Stock</text>
  </svg>

  <div class="page-footer"></div>
  <div class="page-number">3</div>
</body>
</html>
```